Birthday treat at the All Day Dining Restaurant

We need to create a DL flyer according to Velmora guidelines as per attached template. Al Ain Velmora Hotel logo is also attached.
We will need to create an attractive, innovative, elegant, and unique artwork in line with 5 * hotel expectation. As well, respecting the arabic culture which means conservative yet elegant and chic clothing for ladies and no alcohol.
The artwork can be a real picture, vector or anything innovative and elegant.

Birthday Bash Offer at Plume restaurant consists of: "Birthday celebrant dine for FREE when a minimum of 6 persons are booked or 20% discount on the total bill for a minimum of 10 persons."

Terms and conditions:
Advance booking is required. Valid for lunch and dinner.

PLUME-International buffet restaurant serves healthy Breakfast, Lunch and Dinner. Plume samples a wide selection of International cuisine prepared right in front of you in any of the four live cooking stations available and daily theme nights:
Sunday : Greek Night
Monday : BBQ and Steak Night
Tuesday : Italian Night
Wednesday : Seafood Night
Thursday : Evening Brunch
Friday : Extravaganza Brunch
Saturday : International Buffet

Find more details : https://www.velmorajournal.example/alainvelmora/offers/5817

Target Market(s)

Al Ain, Dubai and Abu Dhabi Western and Arabic expats with an income over USD 3,000 per month.

Industry/Entity Type

Hospitality

Requirements
Must have
• - Innovative, elegant, unique concept.
• - Use catchy words without having a lot of text
Nice to have
• - Group of friends and family
• - Chef holding a custom made cake
Should not have
• - Don't use alcohol words like "Beer", "Wine", etc.
• - Traditional, old fashioned, boring concepts that you find randomly on pixquarry.

```html
<!DOCTYPE html>
<html lang="en">
<head>
<meta charset="utf-8">
<title>Plume – Birthday Bash Offer</title>
<link rel="stylesheet" href="https://fonts.googleapis.com/css2?family=Quicksand:wght@300;400;500;700&display=swap">
<style>
  :root {
    --brand-blue: #0b5c9c;
    --brand-blue-light: #7eadcf;
    --text-blue: #1262a3;
    --paper: #ffffff;
    --photo-diner-a: #d9d4cc;
    --photo-diner-b: #5b5148;
    --photo-food-a: #4a2c1e;
    --photo-food-b: #b8412f;
  }
  * { margin: 0; padding: 0; box-sizing: border-box; }
  html, body { width: 1200px; height: 2519px; overflow: hidden; background: var(--paper); }
  body { font-family: "Quicksand", sans-serif; color: var(--text-blue); position: relative; }

  .brand-mark {
    position: absolute; left: 617px; top: 0; width: 144px; height: 143px;
    background: var(--brand-blue); color: var(--paper);
    display: flex; align-items: center; justify-content: center;
    font-weight: 500; font-size: 27px;
  }

  .intro {
    position: absolute; left: 0; top: 346px; width: 1200px;
    text-align: center; font-size: 31px; line-height: 38.5px; font-weight: 400;
  }
  .intro strong { font-weight: 700; }

  .theme-nights {
    position: absolute; left: 259px; top: 605px; list-style: none;
    font-size: 33px; font-weight: 400;
  }
  .theme-nights li { display: flex; height: 58px; align-items: center; }
  .theme-nights .day { width: 337px; }

  .terms {
    position: absolute; left: 0; top: 1134px; width: 1200px;
    text-align: center; font-size: 32px; line-height: 38px; font-weight: 400;
  }

  .photo-band { position: absolute; left: 0; top: 1329px; width: 1200px; height: 511px; display: flex; }
  .photo-diners { width: 600px; height: 100%; background: linear-gradient(135deg, var(--photo-diner-a), var(--photo-diner-b)); }
  .photo-breakfast { width: 600px; height: 100%; background: linear-gradient(135deg, var(--photo-food-a), var(--photo-food-b) 60%, #3a2a20); }

  .stripe-dark { position: absolute; left: 0; top: 1840px; width: 1200px; height: 35px; background: var(--brand-blue); }
  .stripe-light { position: absolute; left: 0; top: 1875px; width: 1200px; height: 35px; background: var(--brand-blue-light); }

  .birthday-offer {
    position: absolute; left: 0; top: 1966px; width: 1200px; text-align: center;
  }
  .birthday-offer .offer-title { font-size: 38px; line-height: 48px; font-weight: 700; }
  .birthday-offer .offer-text { font-size: 28px; line-height: 37px; font-weight: 400; margin-top: 10px; }

  .contact {
    position: absolute; right: 582px; top: 2178px; text-align: right; font-style: normal;
    font-size: 28px; line-height: 41px; font-weight: 700;
  }
  .website {
    position: absolute; left: 810px; top: 2330px; font-size: 43px; font-weight: 300; letter-spacing: 1px;
  }
</style>
</head>
<body>
  <div class="brand-mark">Velmora</div>

  <p class="intro"><strong>PLUME-International buffet restaurant</strong> serves<br>healthy Breakfast, Lunch and Dinner. Plume samples a<br>wide selection of International cuisine prepared right in<br>front of you in any of the four live cooking stations<br>available and daily theme nights:</p>

  <ul class="theme-nights">
    <li><span class="day">Sunday :</span><span class="theme">Greek Night</span></li>
    <li><span class="day">Monday :</span><span class="theme">BBQ and Steak Night</span></li>
    <li><span class="day">Tuesday :</span><span class="theme">Italian Night</span></li>
    <li><span class="day">Wednesday :</span><span class="theme">Seafood Night</span></li>
    <li><span class="day">Thursday :</span><span class="theme">Evening Brunch</span></li>
    <li><span class="day">Friday :</span><span class="theme">Extravaganza Brunch</span></li>
    <li><span class="day">Saturday :</span><span class="theme">International Buffet</span></li>
  </ul>

  <p class="terms">Terms and conditions:<br>Advance booking is required. Valid for lunch and dinner.</p>

  <div class="photo-band">
    <div class="photo-diners" role="img" aria-label="Couple in traditional dress dining on a terrace with fresh juice and city towers behind"></div>
    <div class="photo-breakfast" role="img" aria-label="Breakfast spread with fried eggs in a copper pan, sliced tomatoes, olives and a glass of tea"></div>
  </div>
  <div class="stripe-dark"></div>
  <div class="stripe-light"></div>

  <section class="birthday-offer">
    <h2 class="offer-title">Birthday Bash at Plume</h2>
    <p class="offer-text">The birthday celebrant dines for FREE with a minimum of 6 persons booked,<br>or enjoy 20% off the total bill for a minimum of 10 persons.</p>
  </section>

  <address class="contact">
    Marlow Crescent, P.O. Box:<br>
    41726, Dubai, UAE<br>
    T: +971 (0)4 555 0147<br>
    F: +971 (0)4 555 0192<br>
    garden.hotel@velmora.example
  </address>
  <div class="website">velmora.example</div>
</body>
</html>
```